Dane Morrow films- wedding and event films company website. DESKTOP AND MOBILE

We need a website for a high-end wedding and event film production company. Looking for a very modern and elegant design. my old website is www.danemorrowfilms.example

I like the "white/black/rose gold" color scheme of my logo.

really looking for a sleek modern design the breaths professional and artistic.

Target Market(s)

wedding and event films.

Industry/Entity Type

Film Production

Number of Pages Required

5+ page

Colors

Designer to choose colors to be used in the design.

Requirements
Must have
• website name will be www.danemorrowfilms.example
• tagline is "CINEMATIC STORIES ABOUT YOU"
• sections: HOME, CONTACT, ABOUT, FILMS, BLOG
• You can see my old website at danemorrowfilms.example
• Website about section:
• Dane Morrow Films was Established with the basis of truly cinematic and artistic films in mind. Dane and his team routinely travel the globe documenting weddings and events for high profile clients and discerning couples. Dane was born and raised in Maui Hawaii and has a unique approach to his films that embody the essence of a Hollywood film. Dane has spent the last 10 years traveling the world documenting corporate events and weddings with multiple Award winning production companies. In 2017 Dane decided to establish his own brand “Dane Morrow films” that will take everything he has learned with his past experiences and push it to the next level. Aside from his personal achievements, Dane is extremely passionate about his craft and always looks forward to handcrafting beautiful wedding/event films for his clients. The style of work is non-traditional and the day of filming is extremely unobtrusive (as we are looking for natural-candid/ raw emotions).
• If you are looking for the best price in town, we are probably not the best option, but if you’re looking for the best quality and peace of mind on your wedding day, then you’re in the right place. Dane Morrow Films is a boutique studio that only accepts a limited number of assignments per year. Inquire early to ensure availability.
• LINKS TO VIMEO VIDEOS THAT WILL BE IN THE "FILMS' SECTION.
• BRENT FILM TRAILER - https://clipvault.example/508114362
• BRENT FEATURE FILM - https://clipvault.example/617392048
• JUNE AND ROB'S WEDDING - https://clipvault.example/724958160
• DRONE DEMO REEL - https://clipvault.example/841576203
• WEDDING INDUSTRY EVENT PARTY - https://clipvault.example/962304817/a8d3e7b21c
• images that you can use on site are here: https://brigittolsenimages.proofbox.example/gallery/nora&felix/
• password is: meadow

```html
<!DOCTYPE html>
<html lang="en">
<head>
<meta charset="utf-8">
<title>Dane Morrow Films – Cinematic Stories About You</title>
<link href="https://fonts.googleapis.com/css2?family=Open+Sans:wght@400;600;700&family=Playfair+Display:wght@700&family=Raleway:wght@300;400;600;700&display=swap" rel="stylesheet">
<style>
:root{
  --copper:#e0935a;
  --copper-dark:#c97d45;
  --copper-btn:#d98a50;
  --ink:#2f2f2f;
  --muted:#666;
  --white:#ffffff;
  --frame:#f6d8c0;
}
*{margin:0;padding:0;box-sizing:border-box}
html,body{width:1200px;height:4110px;overflow:hidden}
body{position:relative;background:var(--white);font-family:"Open Sans",Arial,sans-serif;color:var(--ink)}
.abs{position:absolute}
.center-text{left:0;width:1200px;text-align:center}

/* header */
.follow-label{left:78px;top:38px;font-size:14px;font-weight:600}
.social{left:78px;top:62px;display:flex;gap:9px}
.social span{width:40px;height:40px;border-radius:50%;border:2px solid var(--copper)}
.brand{top:52px;font-family:"Raleway",sans-serif;font-weight:600;font-size:26px;letter-spacing:4px;color:var(--ink)}
.call{left:880px;top:38px;display:flex;gap:14px;align-items:flex-start}
.call-label{font-size:14px;font-weight:600;line-height:18px}
.call-number{font-family:"Raleway",sans-serif;font-size:30px;font-weight:600;color:var(--copper);line-height:36px}

/* nav */
.nav{position:absolute;left:0;top:137px;width:1200px;height:63px;background:var(--copper);display:flex;justify-content:center;align-items:center;gap:62px}
.nav a{color:var(--white);text-decoration:none;font-family:"Raleway",sans-serif;font-size:16px;letter-spacing:1px}
.nav a.active{font-weight:700}

/* photos */
.photo{position:absolute}
.hero-photo{left:0;top:200px;width:1200px;height:471px;background:linear-gradient(100deg,#4f6b3a 0%,#7a8d58 28%,#b9b3a2 55%,#d8d3c8 75%,#9aa0a6 100%)}
.zig-up{position:absolute;left:0;width:1200px;height:24px;background:linear-gradient(-45deg,var(--c) 12px,transparent 0),linear-gradient(45deg,var(--c) 12px,transparent 0);background-size:24px 24px;background-repeat:repeat-x;background-position:left bottom}
.zig-down{position:absolute;left:0;width:1200px;height:24px;background:linear-gradient(-135deg,var(--c) 12px,transparent 0),linear-gradient(135deg,var(--c) 12px,transparent 0);background-size:24px 24px;background-repeat:repeat-x;background-position:left top}

.hero-title{top:322px;font-family:"Playfair Display",serif;font-size:58px;color:#f3b27c;text-shadow:0 2px 3px rgba(0,0,0,.45)}
.hero-sub{top:410px;font-family:"Raleway",sans-serif;font-weight:700;font-size:21px;color:var(--white);letter-spacing:1px}
.arrow{top:372px;width:46px;height:46px;border-radius:50%;background:rgba(255,255,255,.35)}

.btn{position:absolute;display:flex;align-items:center;justify-content:center;font-family:"Raleway",sans-serif;font-weight:700;font-size:18px;color:var(--white);background:linear-gradient(#e29a62,#c97d45);border-radius:4px;text-decoration:none;letter-spacing:.5px}
.btn-ghost{background:transparent;border:2px solid var(--white)}

/* welcome */
.welcome{left:0;top:671px;width:1200px;height:480px;background:var(--copper)}
.welcome-frame{left:101px;top:734px;width:406px;height:315px;border:2px solid var(--frame)}
.welcome-photo{left:123px;top:759px;width:376px;height:331px;background:linear-gradient(135deg,#e9e6e0,#9c9891 60%,#3a3a3a)}
.kicker{font-family:"Raleway",sans-serif;font-weight:700;font-size:16px;letter-spacing:1px}
.welcome-kicker{left:556px;top:803px;color:var(--ink)}
.welcome-title{left:554px;top:826px;font-family:"Raleway",sans-serif;font-weight:300;font-size:46px;color:var(--white)}
.welcome-text{left:556px;top:886px;width:500px;font-size:14px;line-height:25px;color:#fff5ec}

/* couple */
.section-kicker{font-family:"Raleway",sans-serif;font-weight:700;font-size:16px;color:var(--ink)}
.section-title{font-family:"Raleway",sans-serif;font-weight:300;font-size:44px;color:var(--copper);letter-spacing:1px}
.portrait{width:258px;height:258px;border-radius:50%;box-shadow:0 4px 12px rgba(0,0,0,.25)}
.quote{top:1610px;font-style:italic;font-size:16px;color:var(--muted)}
.quote-by{top:1648px;font-size:16px;font-weight:700;color:var(--copper)}
.quote-by::before{content:"";display:inline-block;width:24px;height:3px;background:var(--copper);vertical-align:middle;margin-right:14px}

/* films */
.films-photo{left:0;top:1732px;width:1200px;height:666px;background:linear-gradient(180deg,#c9b6a2 0%,#a48870 35%,#6f5a48 70%,#4d3f33 100%)}
.copper-box{background:var(--copper-dark)}
.card{background:var(--white)}
.thumb-films{left:173px;top:1951px;width:339px;height:331px;background:linear-gradient(160deg,#d9dde0,#a4a9a6 55%,#5f5d57)}
.play{position:absolute;width:84px;height:58px;border-radius:14px;background:#e62117}
.play::after{content:"";position:absolute;left:33px;top:17px;border-left:22px solid #fff;border-top:12px solid transparent;border-bottom:12px solid transparent}
.card-title{font-family:"Raleway",sans-serif;font-weight:700;font-size:26px;color:var(--copper);letter-spacing:1px}
.card-text{font-size:14px;line-height:25px;color:var(--muted)}

/* gallery */
.gallery{left:0;top:2480px;width:1200px;height:296px;background:linear-gradient(90deg,#4a4e52 0%,#cfd2d0 14%,#2d3a44 22%,#8d9aa0 28%,#e3e1dc 62%,#7fa8c0 72%,#5f8a5c 82%,#c9c2b6 100%)}
.gallery-feature{left:370px;top:2466px;width:460px;height:329px;background:#c48457;padding:14px}
.gallery-feature div{width:100%;height:100%;border:2px solid var(--frame);background:linear-gradient(135deg,#f2efe8,#a39d93 55%,#3c3a37)}
.dots{top:2830px;left:534px;display:flex;gap:14px}
.dots span{width:18px;height:18px;border-radius:50%;border:2px solid var(--copper)}
.dots span.on{background:var(--copper)}

/* blog */
.blog-photo{left:0;top:2902px;width:1200px;height:660px;background:linear-gradient(180deg,#cbbfb2 0%,#a7998a 40%,#6f6559 75%,#4b443c 100%)}
.thumb-blog{left:611px;top:3118px;width:416px;height:340px;background:linear-gradient(180deg,#8fb6cc 0%,#5d8a7a 35%,#48703f 70%,#6b7a4a 100%)}

/* footer */
.foot-sub{top:3736px;font-family:"Raleway",sans-serif;font-weight:700;font-size:17px;color:var(--ink)}
.foot-title{top:3772px;font-family:"Raleway",sans-serif;font-weight:300;font-size:44px;color:var(--copper);letter-spacing:2px}
.foot-mail{top:3838px;font-size:17px;font-weight:700;color:#a15f30}
.foot-phone{top:3873px;font-size:17px;color:#a15f30}
.foot-bar{left:0;top:4040px;width:1200px;height:70px;background:var(--copper)}
.copyright{top:4068px;font-size:14px;color:var(--white)}
</style>
</head>
<body>

<!-- header -->
<div class="abs follow-label">Follow Us :</div>
<div class="abs social" aria-label="Social links"><span></span><span></span><span></span></div>
<div class="abs center-text brand">DANE MORROW FILMS</div>
<div class="abs call">
  <svg width="46" height="46" viewBox="0 0 24 24" aria-hidden="true"><path fill="#e0935a" d="M6.6 10.8a15 15 0 0 0 6.6 6.6l2.2-2.2c.3-.3.7-.4 1-.2 1.1.4 2.3.6 3.6.6.6 0 1 .4 1 1V20c0 .6-.4 1-1 1A17 17 0 0 1 3 4c0-.6.4-1 1-1h3.5c.6 0 1 .4 1 1 0 1.3.2 2.5.6 3.6.1.3 0 .7-.2 1z"/></svg>
  <div><div class="call-label">Call Us Today :</div><div class="call-number">808 555 0143</div></div>
</div>

<nav class="nav">
  <a class="active" href="#">HOME</a><a href="#">ABOUT</a><a href="#">FILMS</a><a href="#">BLOG</a><a href="#">CONTACT</a>
</nav>

<!-- hero -->
<div class="photo hero-photo" role="img" aria-label="Bride and groom kissing on a stone balustrade terrace beside a garden"></div>
<div class="abs arrow" style="left:18px"></div>
<div class="abs arrow" style="left:1136px"></div>
<div class="abs center-text hero-title">Cinematic Stories About You</div>
<div class="abs center-text hero-sub">HANDCRAFTING BEAUTIFUL WEDDING/EVENT</div>
<a class="btn" href="#" style="left:387px;top:457px;width:208px;height:56px">LEARN MORE</a>
<a class="btn btn-ghost" href="#" style="left:605px;top:457px;width:206px;height:56px">CONTACT US</a>
<div class="zig-up" style="top:647px;--c:var(--copper)"></div>

<!-- welcome -->
<section class="abs welcome"></section>
<div class="abs welcome-frame"></div>
<div class="photo welcome-photo" role="img" aria-label="Black and white portrait of the newlyweds embracing by the sea"></div>
<div class="abs kicker welcome-kicker">WELCOME TO</div>
<h1 class="abs welcome-title">DANE MORROW FILMS</h1>
<p class="abs welcome-text">We pride ourselves on using the best quality cinema tools for our films. The equipment we use are industry standard cinematic tools used in hollywood movies. using such tools gives our films a truely cinematic feel.</p>
<a class="btn" href="#" style="left:556px;top:985px;width:190px;height:46px">LEARN MORE</a>

<!-- happy couple -->
<div class="abs center-text section-kicker" style="top:1208px">OUR</div>
<h2 class="abs center-text section-title" style="top:1230px">HAPPY COUPLE</h2>
<div class="photo portrait" style="left:268px;top:1323px;background:linear-gradient(135deg,#e9c9b4,#b98b74 60%,#6d4f42)" role="img" aria-label="Portrait of the bride smiling"></div>
<div class="photo portrait" style="left:671px;top:1323px;background:linear-gradient(135deg,#d9d9d9,#8a8d93 55%,#20283a)" role="img" aria-label="Portrait of the groom in a navy suit"></div>
<p class="abs center-text quote">“Dane really is one of the best film makers in Hawaii, great work Dane! We loved the film!”</p>
<p class="abs center-text quote-by">Tessa Lyle</p>

<!-- films -->
<div class="photo films-photo" role="img" aria-label="Couple on rocky coastline at sunset"></div>
<div class="zig-down" style="top:1732px;--c:var(--white)"></div>
<div class="abs center-text section-kicker" style="top:1808px;color:var(--white)">OUR</div>
<h2 class="abs center-text section-title" style="top:1830px;color:var(--white)">FILMS</h2>
<div class="abs copper-box" style="left:131px;top:1915px;width:417px;height:414px"></div>
<div class="abs card" style="left:548px;top:1915px;width:520px;height:414px"></div>
<div class="photo thumb-films" role="img" aria-label="Video still of the couple on coastal rocks"></div>
<div class="play" style="left:342px;top:2092px"></div>
<h3 class="abs card-title" style="left:636px;top:2008px">BRENT FILM TRAILER</h3>
<p class="abs card-text" style="left:636px;top:2054px;width:390px">We pride ourselves on using the best quality cinema tools for our films. The equipment we use are industry standard cinematic tools used in hollywood movies. using such tools gives our films a truely cinematic feel.</p>
<a class="btn" href="#" style="left:638px;top:2176px;width:188px;height:52px">WATCH MORE</a>

<!-- gallery -->
<div class="photo gallery" role="img" aria-label="Strip of wedding photos: couple walking on beach, bride and groom, glass tent in garden"></div>
<div class="photo gallery-feature"><div role="img" aria-label="Sepia photo of the couple kissing by the sea"></div></div>
<div class="abs dots"><span></span><span></span><span class="on"></span><span></span><span></span></div>

<!-- blog -->
<div class="photo blog-photo" role="img" aria-label="Rocky seaside cliffs at dusk"></div>
<div class="zig-down" style="top:2902px;--c:var(--white)"></div>
<div class="abs center-text section-kicker" style="top:2974px;color:var(--white)">OUR</div>
<h2 class="abs center-text section-title" style="top:2996px;color:var(--white)">LATEST BLOG POST</h2>
<div class="abs card" style="left:131px;top:3082px;width:521px;height:414px"></div>
<div class="abs copper-box" style="left:652px;top:3082px;width:416px;height:414px"></div>
<div class="photo thumb-blog" role="img" aria-label="Aerial view of a seaside garden venue"></div>
<div class="play" style="left:777px;top:3258px"></div>
<h3 class="abs card-title" style="left:131px;top:3172px;width:521px;text-align:center">LOREM IPSUM IS TEXT</h3>
<p class="abs card-text" style="left:193px;top:3216px;width:400px">Lorem Ipsum is the text simply dummy text of the printing and typesetting industry. Lorem Ipsum has been the industry's standard text Lorem Ipsum is the text simply dummy text of the printing and typesetting industry.</p>
<a class="btn" href="#" style="left:323px;top:3337px;width:239px;height:58px">VIEW ALL BLOG</a>

<!-- footer -->
<div class="abs center-text foot-sub">HANDCRAFTING BEAUTIFUL WEDDING/EVENT</div>
<div class="abs center-text foot-title">CINEMATIC STORIES ABOUT YOU</div>
<div class="abs center-text foot-mail">dane@danemorrowfilms.example</div>
<div class="abs center-text foot-phone">808 555 0143</div>
<a class="btn" href="#" style="left:455px;top:3918px;width:290px;height:56px">BOOK YOUR EVENT</a>
<div class="abs foot-bar"></div>
<div class="zig-up" style="top:4016px;--c:var(--copper)"></div>
<div class="abs center-text copyright">©DANE MORROW FILMS - 2017 All Right Reserved.</div>

</body>
</html>
```